The Quiet Hour Safeguard Handbook

A book cover. The book will be marketed as a promotional item for financial advisors, financial planners, independent insurance agents, bankers, and any professional who views their role as guardian of their clients assets and helping them manage risk.

```html
<!DOCTYPE html>
<html lang="en">
<head>
<meta charset="utf-8">
<title>The Quiet Hour Safeguard Handbook — Cover</title>
<link rel="stylesheet" href="https://fonts.googleapis.com/css2?family=Courier+Prime:ital,wght@0,400;1,700&family=Silkscreen&display=swap">
<style>
  :root {
    --stage: #d6d6d8;
    --night-top: #1d1f4a;
    --night-mid: #221a3e;
    --night-low: #1a1424;
    --ice: #9fd3ea;
    --ice-deep: #6fb6dc;
    --banner-a: #5a90c8;
    --banner-b: #b9e4f3;
    --ink-dark: #141226;
    --art-violet: #5a3a9e;
    --art-blue: #2a7fc8;
  }
  * { margin: 0; padding: 0; box-sizing: border-box; }
  html, body {
    width: 1200px; height: 849px; overflow: hidden;
    background: var(--stage);
  }
  .cover {
    position: absolute; left: 333px; top: 24px;
    width: 533px; height: 800px; overflow: hidden;
    background: linear-gradient(180deg, var(--night-top) 0%, var(--night-mid) 45%, var(--night-low) 70%, var(--night-low) 100%);
    box-shadow: 0 6px 18px rgba(0,0,0,.25);
  }
  .cover__artwork {
    position: absolute; left: 0; top: 0; width: 533px; height: 600px;
    background:
      radial-gradient(ellipse 70% 60% at 75% 20%, rgba(42,127,200,.55), transparent 70%),
      radial-gradient(ellipse 60% 55% at 25% 60%, rgba(90,58,158,.55), transparent 70%);
    -webkit-mask-image: linear-gradient(180deg, #000 0%, #000 65%, transparent 100%);
            mask-image: linear-gradient(180deg, #000 0%, #000 65%, transparent 100%);
  }
  .cover__title {
    position: absolute; left: 0; width: 100%; text-align: center;
    font-family: "Silkscreen", monospace; color: var(--ice);
    line-height: 1; text-transform: uppercase;
    transform-origin: 50% 0;
  }
  .cover__title--the { top: 435px; font-size: 70px; transform: scaleY(1.4); }
  .cover__title--main { top: 511px; font-size: 56px; transform: scaleY(1.7); }
  .cover__subtitle {
    position: absolute; left: 0; width: 100%; top: 614px; text-align: center;
    font-family: "Courier Prime", monospace; font-size: 30px; letter-spacing: 5.5px;
    line-height: 1; color: var(--ice); text-transform: uppercase;
  }
  .cover__banner {
    position: absolute; left: 50px; top: 655px; width: 432px; height: 30px;
    background: linear-gradient(90deg, var(--banner-a), var(--banner-b));
    clip-path: polygon(0 0, 100% 0, 100% 70%, 96% 100%, 4% 100%, 0 70%);
    display: flex; align-items: center; justify-content: center;
    font-family: "Courier Prime", monospace; font-style: italic; font-weight: 700;
    font-size: 13px; letter-spacing: 1px; color: var(--ink-dark);
  }
  .cover__quote {
    position: absolute; left: 0; width: 100%; top: 698px; text-align: center;
    font-family: "Courier Prime", monospace; font-size: 13.3px; letter-spacing: 2px;
    line-height: 18px; color: var(--ice-deep); text-transform: uppercase;
  }
</style>
</head>
<body>
  <main class="cover">
    <div class="cover__artwork" role="img" aria-label="Illustration of a rising bar chart with glowing upward trend lines on a starry night sky"></div>

    <h1 class="cover__heading">
      <span class="cover__title cover__title--the">The</span>
      <span class="cover__title cover__title--main">Quiet Hour</span>
      <span class="cover__subtitle">Safeguard Handbook</span>
    </h1>
    <p class="cover__banner">Protect Yourself and Your Family in the AI Age</p>
    <p class="cover__quote">It’s better to have it and not needed it<br>than need it and not have it.</p>
  </main>
</body>
</html>
```